Croatia Luxury Cruise Brochure

1) Front page instead of By Orchard Path with Liesl please put by Pinecrest Harbor Guild – same on the last page where you have her contacts
2) Can you please add into the second page where you have ‘Welcome to your Croatia trip’ itinerary at glance. You can put it just below the text you have. Create a nice looking table .
D1 August 05, 2023 Arrival to Dubrovnik , Welcome cocktail party on Dubrovnik city walls
D2 August 06, 2023 Dubrovnik Highlights city tour – Embark sail to Elafiti
D3 August 07, 2023 Sail to Mljet island and day at leisure at sea
D4 August 08, 2023 Peljesac Wine Tasting with Live Music – Sail to Korcula
D5 August 09, 2023 Korcula Highlights Explorer Tour & Local Estate Dinner
D6 August 10, 2023 Korcula to Vis Island sail
D7 August 11, 2023 Vis Militarty Tour -sail to Pakleni Islands Bortelli sunset cocktails
D8 August 12, 2023 Hvar island – sail to Split
D9 August 13, 2023 Disembark – Split & Trogir ORVALD tours with 6-course wine dinner
D10 August 14, 2023 Fly out
Note: All tours & Experiences are optional add ons except the Cocktail reception on Dubrovnik city walls
3) Changes to the itinerary:
D1 is now arrival to Dubrovnik day earlier (AUGU5) and the rest is all moved accordingly. Please check the link
https://portal.kelvoro-desk. com/itinerary/custom-trip-prepared-for-liesl-group/
4) Inclusion/Exclusion page we need to update a little. Please make 3 different categories with a note for booking conditions.
Inclusions
• All transfers per itinerary including airport pick up and drop off
• 7 nights cruise on MS Dovetail on half board basis
• All meals stated per itinerary
• Captains dinner
• Unlimited water
• Masseuse on board
• Service of 11 crew members
• Cruise director
• Unlimited WiFi
• Daily cleaning
• Arrival refreshments
• Premium docking
• Usage of non motorized water toys
• Exclusive cocktail reception on Dubrovnik city walls with live music and snacks
Optional Tours
• Dubrovnik Highlights Explorer tour
• Peljesac Wine tour with live music
• Korcula explorer tour with local estate dinner
• Vis Military tour
• Bortelli Lounge bar reservation (min spend EUR100 per person)
• Split & Trogir ORVALD Explorer tour
• 6-course farewell dinner with local wine pairing
• 1 night post stay in Velmont 5* hotel in Split (This is added on optional)
Extras
• Tips for the crew
• Beverage consumption
• Usage of motorized water toys – EUR150 per hour
• International flights
• Any personal expenses
Booking conditions
30 % non-refundable deposit needed upon confirmation
Balance of the trip and any optional tours picked are due 06 May, 2023
Luxury travelers from USA and Canada
Tourism

```html
<!DOCTYPE html>
<html lang="en">
<head>
<meta charset="utf-8">
<title>Croatia Luxury Cruise Brochure – Cruise Price Spread</title>
<link rel="stylesheet" href="https://fonts.googleapis.com/css2?family=Newsreader:wght@400;500&family=Red+Hat+Display:ital,wght@0,500;0,700;1,500&family=DM+Mono:wght@400&display=swap">
<style>
  :root {
    --backdrop: #c9c9c9;
    --brand-red: #d42a1e;
    --ink: #1d1d1f;
    --card: #f4f4f2;
    --rule: #8a8a8a;
    --sky-top: #8fb6d8;
    --sky-low: #dfe6ea;
    --hill: #5a5a3c;
    --sea: #355d86;
    --sea-deep: #16263f;
  }
  * { box-sizing: border-box; margin: 0; padding: 0; }
  html, body { width: 1200px; height: 900px; overflow: hidden; }
  body { background: var(--backdrop); position: relative; }

  .spread {
    position: absolute; left: 100px; top: 96px;
    width: 1000px; height: 707px;
    display: flex;
    box-shadow: 0 10px 30px rgba(0,0,0,.18);
  }
  .page { position: relative; width: 500px; height: 707px; overflow: hidden; }

  .photo-ship-left {
    position: absolute; inset: 0;
    background: linear-gradient(180deg, var(--sky-top) 0%, var(--sky-low) 33%, var(--hill) 36%, #6d6a4a 44%, var(--sea) 47%, var(--sea-deep) 100%);
  }
  .photo-ship-right {
    position: absolute; inset: 0;
    background: linear-gradient(180deg, var(--sky-top) 0%, var(--sky-low) 20%, #9a8a5e 23%, var(--sea) 30%, var(--sea-deep) 70%, #0f1a2c 100%);
  }
  .photo-deck-guests {
    position: absolute; right: 0; bottom: 0; width: 150px; height: 300px;
    background: linear-gradient(160deg, #3d63b8 0%, #2a4a8e 55%, #c99a7a 100%);
  }
  .gutter {
    position: absolute; top: 0; bottom: 0; left: 0; width: 28px;
    background: linear-gradient(90deg, rgba(0,0,0,.25), rgba(0,0,0,0));
  }

  .price-card {
    position: absolute; left: 40px; top: 36px; width: 330px;
    background: var(--card);
    border-radius: 0 0 18px 18px;
    color: var(--ink);
    font-family: "Red Hat Display", sans-serif;
  }
  .price-card__title {
    background: var(--brand-red); color: #fff;
    font-family: "Newsreader", serif; font-weight: 400;
    font-size: 29px; line-height: 1.1;
    padding: 30px 22px 22px;
  }
  .price-card__body { padding: 20px 26px 26px; }
  .section-label {
    color: var(--brand-red); font-weight: 500; font-size: 15px;
    text-transform: uppercase; letter-spacing: .01em;
  }
  .travel-dates { list-style: none; margin: 6px 0 22px; }
  .travel-dates li {
    font-family: "DM Mono", monospace; font-size: 11.5px;
    padding: 6px 0; border-bottom: 1px dotted var(--rule);
  }
  .price-list { list-style: none; margin-top: 8px; }
  .price-row {
    display: flex; justify-content: space-between; align-items: flex-start;
    padding: 10px 0 12px; border-bottom: 1px dotted var(--rule);
  }
  .cabin { font-weight: 700; font-size: 13px; line-height: 1.15; }
  .cabin__note { display: block; color: var(--brand-red); font-weight: 500; font-size: 10.5px; text-transform: uppercase; }
  .fare { text-align: right; }
  .fare__amount { display: block; font-family: "DM Mono", monospace; color: var(--brand-red); font-size: 14px; }
  .fare__unit { display: block; font-weight: 700; font-size: 9px; }
  .booking-terms { margin-top: 22px; }
  .booking-terms .section-label { font-weight: 700; font-size: 10.5px; }
  .booking-terms p { font-weight: 500; font-size: 13px; line-height: 1.3; margin-top: 4px; }
  .booking-terms em { font-style: italic; }
</style>
</head>
<body>
  <main class="spread">
    <section class="page page--left">
      <div class="photo-ship-left" role="img" aria-label="Aerial photo of a white luxury cruise yacht sailing past a forested mountain coastline"></div>
    </section>

    <section class="page page--right">
      <div class="photo-ship-right" role="img" aria-label="Photo of calm Adriatic sea with a rocky headland under blue sky"></div>
      <div class="photo-deck-guests" role="img" aria-label="Photo of guests relaxing with drinks on the sun deck"></div>
      <div class="gutter"></div>

      <article class="price-card">
        <h1 class="price-card__title">All inclusive cruise price.</h1>
        <div class="price-card__body">
          <h2 class="section-label">Travel dates</h2>
          <ul class="travel-dates">
            <li>05 August - 14 August, 2023</li>
            <li>Dubrovnik - Split, 7 nights cruise</li>
          </ul>

          <h2 class="section-label">Prices</h2>
          <ul class="price-list">
            <li class="price-row">
              <span class="cabin">Lower deck cabin<span class="cabin__note">Portholes</span></span>
              <span class="fare"><span class="fare__amount">USD4750.00</span><span class="fare__unit">per person</span></span>
            </li>
            <li class="price-row">
              <span class="cabin">Lower deck cabin<span class="cabin__note">Windows</span></span>
              <span class="fare"><span class="fare__amount">USD4950.00</span><span class="fare__unit">per person</span></span>
            </li>
            <li class="price-row">
              <span class="cabin">Lower deck balcony</span>
              <span class="fare"><span class="fare__amount">USD5250.00</span><span class="fare__unit">per person</span></span>
            </li>
            <li class="price-row">
              <span class="cabin">Upper deck balcony<span class="cabin__note">W/private terrace</span></span>
              <span class="fare"><span class="fare__amount">USD5550.00</span><span class="fare__unit">per person</span></span>
            </li>
          </ul>

          <div class="booking-terms">
            <h2 class="section-label">Booking conditions:</h2>
            <p>30% non-refundable deposit <em>upon confirmation.</em> Balance and optional tours due 06 May, 2023.</p>
          </div>
        </div>
      </article>
    </section>
  </main>
</body>
</html>
```